8" x 11" One Page Flyer for Fence Installation Company

We are looking to promote our business with a new flyer that would be handed out in person to people or put at their mailbox/door at their homes. The flyer needs to be creative and attention-grabbing. I have attached some of our previous flyers and our website information. Do not call or email regarding the flyer. We want the flyer to look professional but also friendly. One page, NOT folded. You can use images from our website at www.MyBraxtonYard.com or our Facebook page at www.Facebook.com/HollowbrookRailsBKT. We are flexible with what photos you can use but there must be photos of OUR fences on the flyer. More photos specifically can also be provided. Colors need to be suitable for a flyer printed on canary yellow in color paper OR white paper.

Target Market(s)

Homeowners that need a new fence

Industry/Entity Type

Construction

Font styles to use
Sans Serif
Other font styles liked:
• HD Colton

Colors
0054AA
0677BA
7BADD7
CADEEF
E8F1F8
0094D4
00A9DD
6FCCEA
C7EBF8
E9F6FB

Requirements
Must have
• Our fence photos - mostly wood fence photos (different designs), SIZE SHOULD BE LETTER SIZE 8" x 11"
Nice to have
• A nice bible verse featured at the bottom of the flyer.
Should not have
• DO NOT COPY THE WEBSITE FORMAT, I WANT SOMETHING UNIQUE. Other people's fence photos, they must all come from our website or facebook page

```html
<!DOCTYPE html>
<html lang="en">
<head>
<meta charset="utf-8">
<title>Hollowbrook Rails – Fence Flyer</title>
<link href="https://fonts.googleapis.com/css2?family=Archivo+Black&family=Montserrat:wght@500;600;700;800&display=swap" rel="stylesheet">
<style>
  :root{
    --blue:#0054aa;
    --blue-mid:#0677ba;
    --cyan:#00a9dd;
    --sky:#e9f6fb;
    --orange:#df963a;
    --ink:#111;
    --white:#fff;
    --stage:#e6e6e6;
  }
  *{margin:0;padding:0;box-sizing:border-box}
  html,body{width:1200px;height:800px;overflow:hidden;background:var(--stage)}
  .flyer{position:absolute;left:298px;top:10px;width:603px;height:780px;background:var(--white);overflow:hidden;font-family:"Montserrat",sans-serif;box-shadow:0 6px 18px rgba(0,0,0,.18)}
  .flyer-shapes{position:absolute;inset:0}
  .brand{position:absolute;left:26px;top:22px;display:flex;align-items:center;gap:10px;color:var(--white)}
  .brand-mark{width:34px;height:34px;background:var(--white)}
  .brand-name{font-weight:800;font-size:15px;line-height:1}
  .brand-phone{font-weight:800;font-size:13px;margin-top:2px}
  .brand-tag{font-size:6.5px;font-weight:600;margin-top:2px}
  .headline{position:absolute;left:32px;top:108px;font-family:"Archivo Black",sans-serif;color:var(--white);font-size:42px;line-height:1.04;letter-spacing:.5px}
  .subhead{position:absolute;left:34px;top:214px;color:var(--white);font-weight:800;font-size:18px;line-height:1.22}
  .accent-dot{position:absolute;left:60px;top:345px;width:56px;height:48px;border-radius:50%;background:var(--orange)}
  .why{position:absolute;left:34px;top:462px;width:250px}
  .why-title{font-family:"Archivo Black",sans-serif;font-size:25px;line-height:1.1;color:var(--ink)}
  .why-lead{color:var(--orange);font-weight:700;font-style:italic;font-size:10.5px;line-height:1.3;margin-top:3px}
  .benefits{list-style:none;margin-top:8px}
  .benefits li{display:flex;align-items:center;gap:8px;font-size:10.5px;font-weight:700;color:var(--ink);line-height:15px}
  .benefits svg{flex:none}
  .showroom{position:absolute;left:52px;top:662px;width:235px;color:var(--blue-mid);font-weight:700;font-size:9.5px;line-height:1.32}
  .gallery{position:absolute;left:290px;top:300px;display:grid;grid-template-columns:repeat(3,96px);grid-template-rows:repeat(3,88px);gap:5px}
  .g1{background:linear-gradient(160deg,#6d6f5c,#b89e70)}
  .g2{background:linear-gradient(160deg,#8b7e5e,#d7b988)}
  .g3{background:linear-gradient(160deg,#c9b184,#8f7a52)}
  .g4{background:linear-gradient(160deg,#b7a37b,#e8d7b2)}
  .g5{background:linear-gradient(160deg,#8fb0cf,#9b8b5f)}
  .g6{background:linear-gradient(160deg,#2c2a28,#6f8a4c)}
  .g7{background:linear-gradient(160deg,#a39775,#dac9a2)}
  .g8{background:linear-gradient(160deg,#d8cbaa,#9d8e66)}
  .g9{background:linear-gradient(160deg,#5b7f3c,#20201f)}
  .icon-phone{position:absolute;left:340px;top:640px}
  .call{position:absolute;left:388px;top:632px;color:var(--white)}
  .call-label{font-weight:800;font-size:13px}
  .call-number{font-family:"Archivo Black",sans-serif;font-size:24px;line-height:1.05}
  .verse{position:absolute;left:360px;top:708px;width:225px;color:var(--white);font-size:7.5px;font-weight:600;line-height:1.35}
  .verse cite{display:block;text-align:right;font-style:normal;font-weight:800}
  .email{position:absolute;left:52px;top:738px;display:flex;align-items:center;gap:10px}
  .email-label{font-weight:800;font-size:11px;color:var(--ink)}
  .email-address{font-weight:600;font-size:12px;color:#333}
</style>
</head>
<body>
<main class="flyer">
  <svg class="flyer-shapes" width="603" height="780" viewBox="0 0 603 780">
    <defs>
      <linearGradient id="picketTones" x1="0" y1="0" x2="1" y2="1">
        <stop offset="0" stop-color="#4e6a2c"/>
        <stop offset=".45" stop-color="#c9a46a"/>
        <stop offset=".75" stop-color="#efe6cf"/>
        <stop offset="1" stop-color="#a89c72"/>
      </linearGradient>
    </defs>
    <rect x="0" y="0" width="603" height="780" fill="var(--sky)" opacity=".5"/>
    <rect x="0" y="0" width="603" height="280" fill="url(#picketTones)" role="img" aria-label="Photo of a white picket fence with pointed posts in a garden"/>
    <polygon points="340,262 470,262 603,100 603,150 505,292 320,292" fill="var(--cyan)"/>
    <polygon points="540,272 603,195 603,272" fill="var(--cyan)"/>
    <polygon points="0,0 300,0 380,290 0,460" fill="var(--blue)"/>
    <polygon points="330,600 603,600 603,780 260,780" fill="var(--blue)"/>
  </svg>

  <div class="brand">
    <span class="brand-mark"></span>
    <div>
      <div class="brand-name">Hollowbrook Rails</div>
      <div class="brand-phone">704-555-0192</div>
      <div class="brand-tag">"Because Good Fences Make Good Neighbors"</div>
    </div>
  </div>

  <h1 class="headline">WE BUILD<br>FENCES</h1>
  <p class="subhead">And we would love to<br>build your fence too!</p>
  <span class="accent-dot"></span>

  <section class="why">
    <h2 class="why-title">Why Choose Us</h2>
    <p class="why-lead">Beautiful, professionally installed fences<br>at affordable prices!</p>
    <ul class="benefits">
      <li><svg width="10" height="10" viewBox="0 0 10 10"><circle cx="5" cy="5" r="5" fill="var(--orange)"/><path d="M2.6 5.2l1.6 1.5 3.2-3.2" stroke="#fff" stroke-width="1.4" fill="none"/></svg>Free Estimates</li>
      <li><svg width="10" height="10" viewBox="0 0 10 10"><circle cx="5" cy="5" r="5" fill="var(--orange)"/><path d="M2.6 5.2l1.6 1.5 3.2-3.2" stroke="#fff" stroke-width="1.4" fill="none"/></svg>Professional Installation</li>
      <li><svg width="10" height="10" viewBox="0 0 10 10"><circle cx="5" cy="5" r="5" fill="var(--orange)"/><path d="M2.6 5.2l1.6 1.5 3.2-3.2" stroke="#fff" stroke-width="1.4" fill="none"/></svg>Concrete in EVERY Post</li>
      <li><svg width="10" height="10" viewBox="0 0 10 10"><circle cx="5" cy="5" r="5" fill="var(--orange)"/><path d="M2.6 5.2l1.6 1.5 3.2-3.2" stroke="#fff" stroke-width="1.4" fill="none"/></svg>HOA Submission Assistance</li>
      <li><svg width="10" height="10" viewBox="0 0 10 10"><circle cx="5" cy="5" r="5" fill="var(--orange)"/><path d="M2.6 5.2l1.6 1.5 3.2-3.2" stroke="#fff" stroke-width="1.4" fill="none"/></svg>Lifetime Workmanship Warranty</li>
      <li><svg width="10" height="10" viewBox="0 0 10 10"><circle cx="5" cy="5" r="5" fill="var(--orange)"/><path d="M2.6 5.2l1.6 1.5 3.2-3.2" stroke="#fff" stroke-width="1.4" fill="none"/></svg>Experienced Installation Teams</li>
      <li><svg width="10" height="10" viewBox="0 0 10 10"><circle cx="5" cy="5" r="5" fill="var(--orange)"/><path d="M2.6 5.2l1.6 1.5 3.2-3.2" stroke="#fff" stroke-width="1.4" fill="none"/></svg>Quality Workmanship &amp; Materials</li>
      <li><svg width="10" height="10" viewBox="0 0 10 10"><circle cx="5" cy="5" r="5" fill="var(--orange)"/><path d="M2.6 5.2l1.6 1.5 3.2-3.2" stroke="#fff" stroke-width="1.4" fill="none"/></svg>FREE Gate Adjustments for LIFE</li>
    </ul>
  </section>

  <p class="showroom">Visit our indoor &amp; outdoor showroom! Our outdoor showroom is open 24/7, while our indoor showroom and office is open Monday - Thurs 9AM - 3PM, Friday 9AM - 1PM</p>

  <div class="email">
    <svg width="30" height="30" viewBox="0 0 30 30"><circle cx="15" cy="15" r="15" fill="var(--cyan)"/><rect x="8" y="10" width="14" height="10" fill="#fff"/><path d="M8 10l7 6 7-6" stroke="var(--cyan)" stroke-width="1.5" fill="none"/></svg>
    <div>
      <div class="email-label">Email Us !</div>
      <div class="email-address">office@mybraxtonyard.com</div>
    </div>
  </div>

  <div class="gallery">
    <div class="g1" role="img" aria-label="Wood rail fence with wire mesh"></div>
    <div class="g2" role="img" aria-label="Long wooden privacy fence"></div>
    <div class="g3" role="img" aria-label="Scalloped wooden picket fence beside a house"></div>
    <div class="g4" role="img" aria-label="Arched wooden gate"></div>
    <div class="g5" role="img" aria-label="Split rail fence in a field"></div>
    <div class="g6" role="img" aria-label="Black aluminum fence"></div>
    <div class="g7" role="img" aria-label="Wooden gate with black hardware"></div>
    <div class="g8" role="img" aria-label="Shadowbox wooden fence"></div>
    <div class="g9" role="img" aria-label="Black metal fence on a lawn"></div>
  </div>

  <svg class="icon-phone" width="34" height="34" viewBox="0 0 34 34"><circle cx="17" cy="17" r="17" fill="var(--cyan)"/><path d="M11 10c1-1 2-1 3 0l1.5 2.5c.5 1 0 1.7-.7 2.3 1 2 2.5 3.5 4.4 4.4.6-.7 1.3-1.2 2.3-.7L24 20c1 1 1 2 0 3-2 2-6 1-9.5-2.5S9 12 11 10z" fill="#fff"/></svg>
  <div class="call">
    <div class="call-label">CALL US TODAY !</div>
    <div class="call-number">704-555-0192</div>
  </div>
  <blockquote class="verse">"In the world you will have tribulation. But take heart; I have overcome the world."<cite>JOHN 16:33</cite></blockquote>
</main>
</body>
</html>
```